Hi, everyone!

We're looking for a tenacious designer to help us create two (2) 33 x 86 single-sided retractable banners. The banners will be purchased through
Plakora (see: https://www.plakora.example/signs-posters/retractable-banners?xnav=swsProductOnly_ResultTitle).

I have attached a wide variety of materials including the Valtrix - Creative Production logos (.psd files), previous attempts at making a banner including some handwritten notes and a table cloth that will be used in the same space as the banners and the back of our business card to give you an idea of our colours.

Note: We like the colours used on the other banner designs but do not like the layout or icons - they look cluttered and unprofessional. They are good as a guide but not what we want as a design. Similarly, avoid featuring close-ups of people from stock photos.

At least one of the banners must feature: (you can use icons instead of words if it means a better design)

www.valtrix.example
Email: hello@valtrix.example
Phone: (555) 318-4702
Social Media Handle: valtrixonward

There is also a word document on the bottom to guide some of the copywriting that may be used. If you're really ambitious, we're happy to consider different phrases and copy.

Finally, the fonts that we use are:
Valtrix Logo - Metropolis
Titles: Adelle Font Family
Body / Content: Avenir Font Family

As with everything, we welcome other suggestions or recommendations.

Target Market(s)

Government, Small Business, Non-Profits, Indigenous Canadian Communities

Font styles to use
Sans Serif

Colors

Designer to choose colors to be used in the design.

Requirements
Must have
• The deliverables for this project are:
• - Two (2) 33 x 86 Single-Sided Retractable Banners
• They will be purchased through Plakora Canada (see: https://www.plakora.example/signs-posters/retractable-banners?xnav=swsProductOnly_ResultTitle). You may want to try loading your design there before submitting them to us.
Nice to have
• We like the colours of the initial designs but they are unprofessional, cluttered and from a template. Ideally, we would like a unique design that works with the colours in our logo (red, black, white and yellow).
• One banner may focus on Tourism Development and the other could feature Creative Strategy.
Should not have
• Please do not use stock photos that feature people - our target market is put off by such pictures. If you'd like an idea of our tourism focus, visit:
• - https://northwaytravelguild.example/en/
• - https://lakelandtrailscouncil.example/
• - https://www.perbo.example/

```html
<!DOCTYPE html>
<html lang="en">
<head>
<meta charset="utf-8">
<title>Valtrix Creative Productions – Retractable Banner</title>
<link rel="stylesheet" href="https://fonts.googleapis.com/css2?family=Hanken+Grotesk:wght@700;800&family=Mulish:ital,wght@0,400;0,700;0,800;1,400;1,800&display=swap">
<style>
  :root {
    --ink: #000000;
    --paper: #ffffff;
    --gold: #e9ab22;
    --crimson: #c22c37;
    --sky: #5d8fc9;
    --sky-light: #c9dbee;
    --hill: #8c9a4a;
    --ground: #7a4a32;
  }
  * { margin: 0; padding: 0; box-sizing: border-box; }
  html, body { width: 1200px; height: 3127px; overflow: hidden; background: var(--ink); }
  .banner {
    position: relative; width: 1200px; height: 3127px; overflow: hidden;
    background: var(--ink); color: var(--paper);
    font-family: "Mulish", "Avenir", sans-serif;
  }
  .hero-art { position: absolute; left: 0; top: 0; width: 1200px; height: 1300px; }
  .headline {
    position: absolute; top: 1334px; left: 0; width: 1200px; text-align: center;
    font-family: "Hanken Grotesk", sans-serif; font-weight: 800;
    font-size: 106px; line-height: 122px; letter-spacing: -1px; white-space: nowrap;
  }
  .accent-gold { color: var(--gold); }
  .accent-red { color: var(--crimson); }
  .tagline {
    position: absolute; top: 1710px; left: 0; width: 1200px; text-align: center;
    font-size: 51px; line-height: 64px; font-weight: 400; white-space: nowrap;
  }
  .tagline em { color: var(--gold); font-style: italic; }
  .intro {
    position: absolute; top: 1804px; left: 85px; width: 1080px;
    font-size: 30px; line-height: 37px; white-space: nowrap;
  }
  .section-title {
    position: absolute; top: 1948px; left: 0; width: 1200px; text-align: center;
    font-family: "Hanken Grotesk", sans-serif; font-weight: 800; font-size: 52px; line-height: 66px;
  }
  .step-band { position: absolute; left: 0; width: 1200px; }
  .step-band svg { position: absolute; left: 0; top: 0; }
  .step-text {
    position: absolute; left: 216px; width: 960px;
    font-size: 25px; line-height: 29px; white-space: nowrap;
  }
  .step-text b { font-weight: 800; }
  .step-on-gold { color: var(--ink); }
  .connected {
    position: absolute; top: 2619px; left: 0; width: 1200px; text-align: center;
    font-size: 35px; line-height: 43px; white-space: nowrap;
  }
  .connected strong { color: var(--gold); font-weight: 700; }
  .cloth-title {
    position: absolute; top: 2740px; left: 0; width: 1200px; text-align: center;
    font-family: "Hanken Grotesk", sans-serif; font-weight: 800; font-size: 37px; line-height: 46px; color: var(--gold);
  }
  .cloth-line {
    position: absolute; top: 2792px; left: 0; width: 1200px; text-align: center;
    font-size: 30px; line-height: 40px; white-space: nowrap;
  }
  .cloth-line em { color: var(--gold); font-weight: 800; font-style: italic; }
  .contact-list { position: absolute; top: 2950px; left: 146px; list-style: none; }
  .contact-list li {
    display: flex; align-items: center; gap: 8px;
    font-size: 24px; font-weight: 800; line-height: 29px; white-space: nowrap;
  }
  .social {
    position: absolute; top: 3004px; left: 440px; width: 260px; text-align: center;
    font-size: 24px; font-weight: 800; line-height: 30px;
  }
  .brand { position: absolute; top: 2960px; left: 825px; width: 320px; height: 90px; }
  .brand-name {
    position: absolute; left: 0; top: 0;
    font-weight: 800; font-size: 54px; line-height: 60px; letter-spacing: 1px; color: var(--paper);
  }
  .brand-sub {
    position: absolute; left: 2px; top: 58px; font-size: 19px; line-height: 24px; font-weight: 400;
    letter-spacing: 1px; color: var(--gold); white-space: nowrap;
  }
</style>
</head>
<body>
<main class="banner">
  <svg class="hero-art" viewBox="0 0 1200 1300" xmlns="http://www.w3.org/2000/svg">
    <defs>
      <linearGradient id="landscape" x1="0" y1="0" x2="0" y2="1">
        <stop offset="0" stop-color="var(--sky)"/>
        <stop offset="0.35" stop-color="var(--sky-light)"/>
        <stop offset="0.55" stop-color="var(--hill)"/>
        <stop offset="1" stop-color="var(--ground)"/>
      </linearGradient>
    </defs>
    <path d="M225 0 C60 170 20 430 110 660 C280 1050 800 1260 1200 1292 V0 Z" fill="var(--gold)"/>
    <path d="M250 0 C90 160 40 420 130 640 C290 1000 800 1190 1200 1225 V0 Z" fill="var(--crimson)"/>
    <path role="img" aria-label="Photograph of a stone inukshuk on Arctic tundra with mountains, a fjord and a blue cloudy sky"
          d="M273 0 C120 150 60 420 150 620 C300 950 800 1120 1200 1145 V0 Z" fill="url(#landscape)"/>
  </svg>

  <h1 class="headline">
    Creating <span class="accent-gold">Meaningful</span><br>
    <span class="accent-gold">Experiences</span> through<br>
    Problem-solving
  </h1>

  <p class="tagline">Redefining <em>Engagement</em> for <span class="accent-red">Real Outcomes</span></p>

  <p class="intro">Our context informs our needs. Our experience and backgrounds in<br>tourism and community development, outdoor recreation, marketing, film<br>production, project management and design ensure those needs are met.</p>

  <h2 class="section-title">Our Approach:</h2>

  <div class="step-band" style="top:2056px;height:86px;">
    <svg width="1200" height="86"><polygon points="161,0 1200,0 1200,86 168,86" fill="var(--gold)"/></svg>
    <p class="step-text step-on-gold" style="top:12px;"><b>Discover</b> – We’re adventures at heart. Our inquisitive nature, cultural knowledge and<br>perspective allows us to understand a challenge and find a suitable solution.</p>
  </div>

  <p class="step-text" style="top:2154px;"><b>Define</b> – Our company comes from a desire to create real outcomes. We work to<br>understand the challenges and opportunities that real people encounter in their<br>lives.</p>
  <p class="step-text" style="top:2270px;">We empower our clients through collective creativity. Our processes your first-hand<br>experience and perspective are included throughout the problem-solving process.</p>
  <p class="step-text" style="top:2358px;">Your experience is at the core of our services. Shaped by our experience in the<br>hospitality industry so all services made are accessible, customer-focused and</p>

  <div class="step-band" style="top:2432px;height:86px;">
    <svg width="1200" height="86"><polygon points="172,0 1200,0 1200,86 166,86" fill="var(--crimson)"/></svg>
    <p class="step-text" style="top:12px;"><b>Design</b> – Opportunities understanding of observed, human need. The services we<br>provided are all focused on meaningful and useful experiences for people.</p>
  </div>

  <p class="step-text" style="top:2528px;"><b>Deliver</b> – We provide services across the entire customer journey. Our services all<br>present an opportunity to learn more and build on</p>

  <p class="connected">Our <strong>connected approach</strong> shapes everything that we do.<br>Whether it’s insights, events or marketing, we’re</p>

  <h3 class="cloth-title">Tablecloth Design</h3>
  <p class="cloth-line">Harness the power of story to <em>learn, share, elevate and innovate.</em></p>

  <ul class="contact-list">
    <li>
      <svg width="24" height="24" viewBox="0 0 24 24"><circle cx="12" cy="12" r="10" fill="none" stroke="var(--crimson)" stroke-width="2.5"/><ellipse cx="12" cy="12" rx="4" ry="10" fill="none" stroke="var(--crimson)" stroke-width="2"/><line x1="2" y1="12" x2="22" y2="12" stroke="var(--crimson)" stroke-width="2"/></svg>
      www.valtrix.example
    </li>
    <li>
      <svg width="24" height="24" viewBox="0 0 24 24"><rect x="2" y="5" width="20" height="14" rx="2" fill="var(--crimson)"/><polyline points="2,6 12,13 22,6" fill="none" stroke="var(--ink)" stroke-width="2"/></svg>
      hello@valtrix.example
    </li>
    <li>
      <svg width="24" height="24" viewBox="0 0 24 24"><rect x="2" y="2" width="20" height="20" rx="4" fill="var(--crimson)"/><path d="M8 6 L10 9 L9 11 C10 13 11 14 13 15 L15 14 L18 16 L17 18 C12 18 6 12 6 7 Z" fill="var(--ink)"/></svg>
      (555) 318-4702
    </li>
  </ul>

  <p class="social">@valtrixonward</p>

  <div class="brand">
    <span class="brand-name">VALTRIX</span>
    <span class="brand-sub">CREATIVE PRODUCTIONS</span>
  </div>
</main>
</body>
</html>
```